larvosk.net

We are a IT Service for the valley. I want a clean website, with new Design, like animated pictures. We focus on IT. Give me your best design. What I'm looking for is eye catching. Works with Smart Phones, and iPad, Tab. Need a section for Submit a support tickets and Remote support. I'm looking for new ideals. I'm open mind, let me see what you guys can do.

Target Market(s)

My clients to see what service and products we have.

Industry/Entity Type

It Service

Requirements
Must have
• Able to submit a trouble tickets and works with Smart Phones, iPad, Tab.

```html
<!DOCTYPE html>
<html lang="en">
<head>
<meta charset="utf-8">
<title>Larvosk Technology</title>
<link href="https://fonts.googleapis.com/css2?family=Ubuntu:wght@400;500;700&family=Open+Sans:wght@400;600&display=swap" rel="stylesheet">
<style>
:root{
  --red:#d42a2a;--navy:#243f6b;--blue:#1a74ae;--blue-dark:#11598a;
  --text:#555;--muted:#9a9a9a;--line:#e3e3e3;--panel:#f5f5f5;
  --footer:#3a3a3a;--footer-deep:#2c2c2c;--footer-text:#b8b8b8;
}
*{margin:0;padding:0;box-sizing:border-box}
html,body{width:893px;height:1200px;overflow:hidden;background:#fff;font-family:"Open Sans",sans-serif;color:var(--text)}
.page{position:relative;width:893px;height:1200px}
.abs{position:absolute}
.topbar{left:0;top:0;width:893px;height:5px;background:#1a1a1a}
.header-rule{left:8px;top:72px;width:885px;height:1px;background:var(--line)}
.brand{left:108px;top:18px;display:flex;align-items:center;gap:8px}
.brand-mark{width:16px;height:16px;background:var(--red)}
.brand-name{font-family:"Ubuntu",sans-serif;font-weight:500;font-size:21px;color:var(--navy);letter-spacing:.5px}
.nav{left:456px;top:5px;display:flex}
.nav a{display:block;text-decoration:none;text-align:center;height:68px;padding-top:21px}
.nav .t{display:block;font-family:"Ubuntu",sans-serif;font-weight:700;font-size:10.5px;color:var(--red)}
.nav .s{display:block;font-size:7.5px;font-style:italic;color:#b5b5b5;margin-top:2px}
.nav .active{background:#f4f4f4;border-bottom:2px solid var(--red);border-top:3px solid var(--red);padding-top:18px}
.hero{left:82px;top:91px;width:729px;height:348px;background:linear-gradient(100deg,#d9dce0 0%,#b8bdc4 40%,#4a4f57 62%,#2c3036 100%)}
.hero-tag{left:82px;top:310px;width:262px;height:93px;background:rgba(110,110,110,.75);padding:9px 0 0 23px;color:#fff;font-family:"Ubuntu",sans-serif}
.hero-tag .a{font-size:14px;font-weight:500}
.hero-tag .b{font-size:36px;font-weight:500;line-height:36px}
.hero-tag .c{font-size:15px;font-weight:500;letter-spacing:.5px}
.intro{left:82px;top:439px;width:729px;height:78px;background:var(--panel);border-top:2px solid #d8d8d8;border-bottom:2px solid #d8d8d8}
.intro h1{position:absolute;left:28px;top:17px;font-family:"Ubuntu",sans-serif;font-weight:400;font-size:14.5px;color:var(--navy)}
.intro p{position:absolute;left:28px;top:38px;width:510px;font-size:8px;line-height:12px;color:#777}
.btn-big{position:absolute;left:553px;top:21px;width:153px;height:39px;background:linear-gradient(#2a86c4,var(--blue-dark));color:#fff;font-family:"Ubuntu",sans-serif;font-size:14px;text-align:center;line-height:39px}
.section-title{font-family:"Ubuntu",sans-serif;font-weight:700;font-size:12px;color:var(--navy)}
.prod-title{left:91px;top:539px}
.prod-rule{left:82px;top:561px;width:729px;height:1px;background:var(--line)}
.product{top:576px;width:165px}
.product .pic{height:105px;background:radial-gradient(circle,#fff 40%,#ececec 100%);border:1px solid #eee;display:flex;align-items:center;justify-content:center}
.product .pic span{display:block;width:80px;height:58px;border-radius:6px;background:linear-gradient(#555,#222)}
.product h3{font-family:"Ubuntu",sans-serif;font-weight:400;font-size:11px;letter-spacing:.5px;color:#444;text-align:center;margin-top:10px}
.product p{font-size:8px;color:#aaa;text-align:center;margin-top:5px;letter-spacing:.3px}
.product .rule{height:1px;background:var(--line);margin-top:12px}
.info{left:81px;top:754px;width:730px;height:316px;background:var(--panel);border:1px solid var(--line)}
.info .head{position:absolute;left:0;top:0;width:100%;height:36px;border-bottom:1px solid var(--line)}
.info .sep{position:absolute;top:36px;width:1px;height:280px;background:var(--line)}
.col{position:absolute;top:14px}
.col ul{list-style:none;margin-top:24px}
.why li{position:relative;padding-left:14px;font-size:8px;line-height:12px;color:#999;margin-bottom:19px;width:200px}
.why li b{color:#444;font-weight:600}
.why li::before,.what li::before{content:"";position:absolute;left:0;top:5px;width:3px;height:3px;border-radius:50%;background:#bbb}
.what li{position:relative;padding-left:15px;margin-bottom:14px;width:215px}
.what h4{font-family:"Ubuntu",sans-serif;font-weight:500;font-size:10.5px;color:#444;margin-bottom:7px}
.what p{font-size:8px;line-height:12px;color:#999}
.support h4{font-family:"Ubuntu",sans-serif;font-weight:500;font-size:10px;color:#444;line-height:12px;width:200px}
.support p{font-size:8px;line-height:12px;color:#888;width:210px;margin-top:12px}
.btn{display:block;width:206px;height:25px;background:linear-gradient(#2a86c4,var(--blue-dark));color:#fff;font-family:"Ubuntu",sans-serif;font-size:10px;text-align:center;line-height:25px;margin-top:10px}
.footer{left:0;top:1070px;width:893px;height:100px;background:var(--footer)}
.footer-notch{left:432px;top:1070px}
.fnav{left:88px;top:1091px;display:flex;font-size:7.5px;color:var(--footer-text)}
.fnav span{padding:0 11px;border-right:1px solid #555}
.fnav span:first-child{padding-left:10px}
.fnav span:last-child{border:0}
.frule{left:90px;top:1119px;width:522px;height:1px;background:#4e4e4e}
.frule2{left:626px;top:1119px;width:164px;height:1px;background:#4e4e4e}
.contact{left:92px;top:1128px;display:flex;gap:18px;align-items:center;font-size:8.3px;color:var(--footer-text)}
.contact div{display:flex;align-items:center;gap:6px}
.stay{left:626px;top:1100px;font-size:7.5px;color:#999}
.social{left:626px;top:1127px;display:flex;gap:14px}
.social span{width:12px;height:12px;background:#666}
.social span.r{border-radius:50%}
.bottom{left:0;top:1170px;width:893px;height:30px;background:var(--footer-deep);display:flex;align-items:center;padding-left:91px;font-size:8.5px;color:#999}
.bottom .name{font-family:"Ubuntu",sans-serif;font-size:9.5px;color:#bbb;margin-right:7px}
.bottom .link{border-left:1px solid #555;padding:0 12px;margin-left:12px}
</style>
</head>
<body>
<div class="page">
  <div class="abs topbar"></div>
  <div class="abs brand"><span class="brand-mark"></span><span class="brand-name">LARVOSK TECHNOLOGY</span></div>
  <nav class="abs nav">
    <a class="active" style="width:82px"><span class="t">HOME</span><span class="s">all starts here</span></a>
    <a style="width:102px"><span class="t">SERVICES</span><span class="s">work we are proud of</span></a>
    <a style="width:86px"><span class="t">PRODUCT</span><span class="s">all the different stuff</span></a>
    <a style="width:100px"><span class="t">CONTACT</span><span class="s">enquire here</span></a>
  </nav>
  <div class="abs header-rule"></div>

  <div class="abs hero" role="img" aria-label="Photo of a technician working on a laptop beside server racks"></div>
  <div class="abs hero-tag"><div class="a">Welcome to</div><div class="b">Larvosk</div><div class="c">Technology</div></div>

  <section class="abs intro">
    <h1>Welcome to Larvosk Technology</h1>
    <p>Founded in 2004, Larvosk Technology focus on quality of their products, along with their customer service to ensure both lengthy uptimes while also minimizing downtime.</p>
    <a class="btn-big">Read More !</a>
  </section>

  <h2 class="abs section-title prod-title">OUR PRODUCTS</h2>
  <div class="abs prod-rule"></div>
  <div class="abs product" style="left:81px"><div class="pic" role="img" aria-label="Desktop workstation with monitor"><span></span></div><h3>Work Station</h3><p>Lorem ipsum dolor sit amet,</p><div class="rule"></div></div>
  <div class="abs product" style="left:268px"><div class="pic" role="img" aria-label="Office desk phone"><span></span></div><h3>Phone System</h3><p>Lorem ipsum dolor sit amet,</p><div class="rule"></div></div>
  <div class="abs product" style="left:455px"><div class="pic" role="img" aria-label="Wide format copier"><span></span></div><h3>Wide Format Copier</h3><p>Lorem ipsum dolor sit amet,</p><div class="rule"></div></div>
  <div class="abs product" style="left:642px"><div class="pic" role="img" aria-label="Software disc"><span style="width:60px;height:60px;border-radius:50%;background:radial-gradient(circle,#eef4fb 15%,#6f9fd0 60%,#2e5f98 100%)"></span></div><h3>Softwares</h3><p>Lorem ipsum dolor sit amet,</p><div class="rule"></div></div>

  <section class="abs info">
    <div class="head"></div>
    <div class="sep" style="left:243px"></div>
    <div class="sep" style="left:487px"></div>
    <div class="col why" style="left:16px">
      <h2 class="section-title">WHY CHOOSE US?</h2>
      <ul>
        <li><b>Accessibility</b> - On-Call and ready to serve your needs. Service is only a call away.</li>
        <li><b>Quality Products</b> - Provide hardware or software that will suit your specific needs.</li>
        <li><b>Consultation</b> - We consult you on proper upgrades or purchases for your company.</li>
        <li><b>Turn Around Time</b> - We Fix your network problem in a timely manner.</li>
        <li><b>Longevity</b> - Building a long-term, trusting, relationship is our goal.</li>
        <li><b>Troubleshooting</b> - We will solve your network problems with a friendly smile.</li>
      </ul>
    </div>
    <div class="col what" style="left:259px">
      <h2 class="section-title">WHAT WE DO?</h2>
      <ul>
        <li><h4>Voxline VOIP Phones</h4><p>Deployment, Management, Instruction of cost effective VOIP Systems for Home/Office.</p></li>
        <li><h4>Business Server</h4><p>Reseller of Corvane RackEdge Servers, Deploy-ment Management, including Mail Exchange</p></li>
        <li><h4>Desktop Workstation</h4><p>Reseller of Corvane Workstation, Corvane OS Pro, Business &amp; Ultimate editions.</p></li>
        <li><h4>Website</h4><p>- Creation &amp; Design<br>- Domain Control/Hosting<br>- E-Mail, Web forwarding</p></li>
      </ul>
    </div>
    <div class="col support" style="left:501px">
      <h2 class="section-title">NEED PRODUCT SUPPORT?</h2>
      <h4 style="margin-top:23px">Request Assistance from Our Support Team:</h4>
      <p>Our expert technical support team is ready to help you. To properly route your inquiry, please submit a support ticket.</p>
      <a class="btn">Submit a technical Support Ticket &gt;&gt;</a>
      <h4 style="margin-top:23px">Get Immediate Answer Online:</h4>
      <p>Many customers find their support questions are answered in our extensive knowledge base and product documentation. To resolve your issue as quickly as possible, we recommend that you search our online resources:</p>
      <a class="btn" style="margin-top:13px">Submit Online Support resources</a>
    </div>
  </section>

  <footer>
    <div class="abs footer"></div>
    <svg class="abs footer-notch" width="16" height="8" viewBox="0 0 16 8"><path d="M0 0H16L8 8Z" fill="#fff"/></svg>
    <div class="abs fnav"><span>HOME</span><span>SERVICES</span><span>PRODUCT</span><span>CONTACT</span></div>
    <div class="abs stay">STAY CONNECTED</div>
    <div class="abs frule"></div>
    <div class="abs frule2"></div>
    <div class="abs contact">
      <div><svg width="11" height="10" viewBox="0 0 11 10"><path d="M5.5 0L11 5H9.5V10H6.5V7H4.5V10H1.5V5H0Z" fill="#777"/></svg>18 Orchard Lane. Fresno Valley, CA 93700. USA</div>
      <div><svg width="10" height="10" viewBox="0 0 10 10"><path d="M2 0L4 2.5 3 4Q4.5 6.5 6 7L7.5 6 10 8 8.5 10Q3 9 0 1.5Z" fill="#777"/></svg>(555) 014-2298</div>
      <div><svg width="12" height="9" viewBox="0 0 12 9"><rect width="12" height="9" fill="#777"/><path d="M0 0L6 5 12 0" stroke="#3a3a3a" fill="none"/></svg>contact@larvosk.net</div>
    </div>
    <div class="abs social"><span class="r"></span><span></span><span class="r"></span><span></span><span class="r"></span><span></span></div>
    <div class="abs bottom"><span class="name">LARVOSK Techonology</span>© 2012<span class="link">Legal Notice</span><span class="link" style="margin-left:0">Terms</span></div>
  </footer>
</div>
</body>
</html>
```